Business Card Design for Marketing Firm

Looking for business card design for higher end marketing firm. Clean but impressionable/trendy. We are a marketing firm that represents manufacturers in the foodservice equipment and supply industry. Our customers are end users such has hotels, restaurants, country clubs, convention centers and casinos as well as distributors of restaurants supplies and equipment, and manufacturers of foodservice equipment and supplies.
Target Market(s)
Hotels, Restaurants, Supply & Equipment Distributors, Foodservice Manufacturers
Industry/Entity Type
Foodservice/Hospitality
Contact Information for Business Card
Name, Title, Contact Number, Email, Website, Social Media, Address
Requirements
Must have
- Clean & Simple but Serious and Impressionable

```html
<!DOCTYPE html>
<html lang="en">
<head>
<meta charset="utf-8">
<title>Harbor Table Reps – Business Cards</title>
<link href="https://fonts.googleapis.com/css2?family=Open+Sans:wght@400;600;700&display=swap" rel="stylesheet">
<style>
  :root {
    --backdrop: #d1d1d1;
    --card: #f2f2f0;
    --ink-blue: #2b2a8c;
    --ink-grey: #8c8c8c;
  }
  * { box-sizing: border-box; margin: 0; padding: 0; }
  html, body { width: 1200px; height: 1051px; overflow: hidden; }
  body {
    background: var(--backdrop);
    font-family: "Open Sans", Arial, sans-serif;
    display: flex;
    flex-direction: column;
    align-items: center;
    justify-content: center;
    gap: 80px;
  }
  .card {
    width: 560px;
    height: 320px;
    background: var(--card);
    border-bottom: 5px solid var(--ink-blue);
    box-shadow: 0 14px 30px rgba(0,0,0,0.12);
    position: relative;
  }
  .brand-name {
    color: var(--ink-blue);
    font-weight: 600;
    text-transform: uppercase;
    letter-spacing: 0.06em;
    line-height: 1.15;
    text-align: right;
  }
  /* Front */
  .card-front { display: flex; align-items: center; justify-content: center; }
  .card-front .brand-name { font-size: 30px; }
  /* Back */
  .card-back { display: flex; padding: 44px 36px 0 36px; }
  .card-back .brand-block {
    width: 230px;
    padding-top: 40px;
    padding-right: 22px;
  }
  .card-back .brand-name { font-size: 19px; }
  .divider {
    width: 1.5px;
    height: 190px;
    background: var(--ink-blue);
    margin-right: 24px;
  }
  .contact { color: var(--ink-grey); font-size: 13px; line-height: 1.45; }
  .person-name {
    color: var(--ink-blue);
    font-weight: 700;
    font-size: 18px;
    text-transform: uppercase;
    letter-spacing: 0.04em;
  }
  .person-title { margin-bottom: 14px; }
  .address { margin-bottom: 10px; }
  .contact-line { display: flex; align-items: center; gap: 7px; }
  .contact-line svg { width: 11px; height: 11px; fill: var(--ink-blue); flex: none; }
  .social {
    position: absolute;
    left: 100px;
    bottom: 26px;
    display: flex;
    align-items: center;
    gap: 8px;
    color: var(--ink-grey);
    font-size: 13px;
  }
  .social-dot { width: 12px; height: 12px; border-radius: 50%; background: var(--ink-blue); }
</style>
</head>
<body>
  <section class="card card-front">
    <div class="brand-name">Harbor Table<br>Reps</div>
  </section>

  <section class="card card-back">
    <div class="brand-block">
      <div class="brand-name">Harbor Table<br>Reps</div>
    </div>
    <div class="divider"></div>
    <div class="contact">
      <div class="person-name">Dorian Vale</div>
      <div class="person-title">President</div>
      <div class="address">1870 Cove Landing Dr<br>Seaside CA 93955</div>
      <div class="contact-line">
        <svg viewBox="0 0 24 24" aria-hidden="true"><path d="M6.6 10.8a15 15 0 0 0 6.6 6.6l2.2-2.2c.3-.3.7-.4 1-.2 1.1.4 2.3.6 3.6.6.6 0 1 .4 1 1V20c0 .6-.4 1-1 1A17 17 0 0 1 3 4c0-.6.4-1 1-1h3.5c.6 0 1 .4 1 1 0 1.3.2 2.5.6 3.6.1.3 0 .7-.2 1z"/></svg>
        555-014-2736
      </div>
      <div class="contact-line">
        <svg viewBox="0 0 24 24" aria-hidden="true"><path d="M2 5h20v14H2zM3.5 6.5 12 13l8.5-6.5z" fill-rule="evenodd"/></svg>
        info@harbortablereps.com
      </div>
      <div class="contact-line">
        <svg viewBox="0 0 24 24" aria-hidden="true"><circle cx="12" cy="12" r="10"/></svg>
        www.harbortablereps.com
      </div>
    </div>
    <div class="social">
      <span class="social-dot"></span>
      @harbortablereps
    </div>
  </section>
</body>
</html>
```